Qortvax@mailvane.net

I am making this a landing page and I want to really grab the person and get them to call. So, I want some up front language at the top language about why they should contact me right away. The person looking is in a tough spot, they woe a lot of debt, they do not want to file a bankruptcy for moral or personal reasons, I want them to know that bankruptcy is a legal process that can help them and that they should not fear checking out their options. I will give them all of the information and if they want to go further fine, if not, they will have a lot more information about their situation and options

The language at the top, I want to be

Thanks for visiting us. You came here because you are having debt problems and you want solutions. Yes, we want your business. But, we don't want it if it is not right for you. We have been at this a long time and assisted thousands of Hawaii people and families with their debt problems. Many of those people were referred by former clients, but, our biggest referral source is people who did not file a bankruptcy. The reason is simple- our absolutely free and confidential consultation will help you get a handle on your whole situation. We will discuss your assets, your debts, your income and expenses and get a complete picture. It is only with this complete global picture of your particular situation that you can know your options, all of them, and then you can decide what is right for you. You are the driver. Call us at 472-3000 (from all islands) and let us help you today!

The color should be calming without being wimpy.

i want the top to be simple and a call to action giving people the sense that we know what we are doing and that they can call us for truly no obligation and we can help them diagnose their money issues and I can give them their options and they can do whatever they wish with them.

Hawaii people between ages of 28-70 who have credit card, loan or mortgage problems and need a way to get out of their debt

Legal

• Must incorporate the items at plkwindra.com. May be helpful to look at owezerozumbo.com for example of the "clean clear" landing I would like to "grab" the customer's attention and get them to call me, phone is better than email. So must have contact us too.

```html
<!DOCTYPE html>
<html lang="en">
<head>
<meta charset="utf-8">
<title>Daniel K. Halvorsen, Attorney At Law</title>
<link rel="stylesheet" href="https://fonts.googleapis.com/css2?family=EB+Garamond:wght@400;500;600&family=Tinos:wght@400;700&family=Arimo:wght@400;700&display=swap">
<style>
  :root {
    --page: #ffffff;
    --royal: #2f5ee8;
    --sky-top: #4b78de;
    --sky-low: #c9d9f1;
    --panel: #ffffff;
    --soft: #f1f2f4;
    --ink: #1b1b1b;
    --muted: #555a60;
    --link: #3b6fe0;
    --title-blue: #2a63c9;
    --gold: #f2c218;
    --line: #c9ced6;
    --wood: #8a5530;
    --steel: #9aa0a8;
    --figure: #dfe3ea;
  }
  * { box-sizing: border-box; margin: 0; padding: 0; }
  html, body { width: 1200px; height: 1200px; overflow: hidden; background: var(--page); }
  body { position: relative; font-family: "Tinos", serif; color: var(--ink); }

  .site { position: absolute; left: 97px; top: 30px; width: 1000px; height: 1170px; background: var(--sky-low); }

  .header-scene {
    position: absolute; left: 0; top: 0; width: 1000px; height: 300px;
    background: linear-gradient(180deg, var(--sky-top) 0%, #6f95e3 35%, #9fb6e0 55%, #d6e2f3 75%, #e9eef7 100%);
  }
  .brand-plate {
    position: absolute; left: 33px; top: 32px; width: 386px; height: 122px;
    background: linear-gradient(180deg, #ffffff, #e4e6ea);
    border: 2px solid #b8bcc3; box-shadow: 2px 3px 6px rgba(0,0,0,.35);
    text-align: center; font-family: "EB Garamond", serif;
  }
  .brand-plate .name { margin-top: 10px; font-size: 38px; color: var(--title-blue); line-height: 1.1; }
  .brand-plate .rule { width: 316px; height: 3px; background: var(--title-blue); margin: 4px auto 2px; }
  .brand-plate .role { font-size: 33px; color: var(--title-blue); line-height: 1.1; }

  .gavel-art {
    position: absolute; left: 51px; top: 135px; width: 170px; height: 117px; z-index: 3;
    background: linear-gradient(160deg, #a86a3c, var(--wood)); border-radius: 8px;
  }
  .phone-handset {
    position: absolute; left: 678px; top: 25px; width: 40px; height: 110px;
    background: linear-gradient(90deg, #b4b9c0, var(--steel)); border-radius: 14px;
  }
  .phone-cord {
    position: absolute; left: 703px; top: 145px; width: 195px; height: 34px;
    background: #3a3d44; border-radius: 6px;
  }
  .cta { position: absolute; left: 722px; top: 42px; font-family: "EB Garamond", serif; font-size: 32px; line-height: 31px; text-shadow: 1px 2px 2px rgba(0,0,0,.55); }
  .cta .free { color: #fff; padding-left: 10px; }
  .cta .call { color: var(--gold); }

  .nav {
    position: absolute; left: 270px; top: 183px; width: 699px; height: 47px;
    background: var(--royal); border-radius: 10px 10px 0 0;
    font-family: "EB Garamond", serif; font-size: 24px;
  }
  .nav a { position: absolute; bottom: 0; color: #fff; text-decoration: none; height: 38px; line-height: 42px; white-space: nowrap; }
  .nav .current { left: 9px; width: 83px; text-align: center; background: #fff; color: #222; }

  .content { position: absolute; left: 31px; top: 230px; width: 938px; height: 666px; background: var(--panel); }
  .hero-art {
    position: absolute; left: 17px; top: 15px; width: 615px; height: 318px;
    background: linear-gradient(135deg, #7c8a70, #c9cbbf 40%, #8d9788 65%, #e2e3dc);
  }

  .consult-box { position: absolute; left: 651px; top: 15px; width: 273px; height: 320px; background: var(--soft); font-family: "Arimo", sans-serif; color: var(--muted); }
  .consult-box h2 { font-size: 18px; color: var(--link); font-weight: 700; margin: 2px 0 0 5px; }
  .consult-box .intro { font-size: 12px; line-height: 17px; margin: 14px 6px 0 6px; }
  .field { position: absolute; left: 6px; font-size: 12px; }
  .field span { display: inline-block; width: 87px; }
  .field i { position: absolute; left: 87px; top: -6px; width: 176px; height: 24px; background: #fff; border: 1px solid #dfe2e6; border-radius: 4px; }
  .field.msg i { height: 64px; }
  .req { position: absolute; left: 95px; top: 270px; font-size: 9px; color: #9a9ea5; }
  .submit { position: absolute; left: 172px; top: 284px; width: 93px; height: 23px; border-radius: 4px; background: linear-gradient(#4f8cf7, #2c63e0); color: #fff; font-size: 14px; text-align: center; line-height: 23px; }

  .welcome { position: absolute; left: 13px; top: 348px; width: 615px; font-size: 15px; line-height: 17.7px; }
  .welcome .lead { color: var(--link); font-weight: 700; }
  .welcome em { color: var(--link); }
  .welcome b { color: var(--link); }
  .video {
    float: right; width: 275px; height: 235px; margin: 5px 0 6px 24px; position: relative;
    background: linear-gradient(180deg, #6c6a62, #4a4b4f 70%, #1d1d1f 86%);
  }
  .video .bar { position: absolute; left: 0; bottom: 0; width: 100%; height: 30px; background: #1a1a1a; border-top: 3px solid #444; }
  .video svg { position: absolute; left: 119px; top: 91px; }

  .testimonials { position: absolute; left: 647px; top: 355px; width: 279px; height: 288px; background: var(--soft); font-family: "Arimo", sans-serif; color: var(--muted); padding: 14px 9px 0 9px; }
  .testimonials h2 { font-size: 21px; font-weight: 400; color: var(--title-blue); margin-bottom: 6px; }
  .testimonials p { font-size: 12px; line-height: 18.3px; letter-spacing: -0.2px; white-space: nowrap; padding-bottom: 12px; border-bottom: 2px dashed var(--line); margin-bottom: 16px; }
  .testimonials .more { position: absolute; right: 14px; bottom: 3px; color: var(--link); font-size: 14px; }

  .footer {
    position: absolute; left: 0; top: 896px; width: 1000px; height: 274px;
    background: radial-gradient(ellipse at 60% 60%, #5b93f5, #3a6cec 55%, #2d58dc);
  }
  .map-area { position: absolute; left: 41px; top: 23px; width: 242px; height: 168px; background: linear-gradient(135deg, #efe7d6, #e4dcc9 50%, #d8d1bd); }
  .address { position: absolute; left: 307px; top: 21px; color: #fff; font-family: "EB Garamond", serif; font-size: 18px; line-height: 21.5px; text-shadow: 1px 1px 2px rgba(0,0,0,.4); }
  .address .firm { font-weight: 600; font-size: 22px; line-height: 24px; }
  .address .title { font-weight: 600; }
  .badge { position: absolute; left: 591px; top: 39px; width: 69px; height: 101px; background: #6f94cf; border: 1px solid #9fb7e2; }
  .figure-art { position: absolute; left: 773px; top: 29px; width: 185px; height: 185px; border-radius: 10px; background: linear-gradient(160deg, #eef0f4, var(--figure)); }
  .legal { position: absolute; left: 41px; top: 206px; color: #fff; font-family: "EB Garamond", serif; font-size: 19px; text-shadow: 1px 1px 2px rgba(0,0,0,.4); }
  .legal b { font-weight: 600; }
</style>
</head>
<body>
<div class="site">
  <div class="header-scene" role="img" aria-label="Hawaiian beach and ocean under a blue sky"></div>
  <div class="brand-plate">
    <div class="name">Daniel K. Halvorsen</div>
    <div class="rule"></div>
    <div class="role">Attorney At Law</div>
  </div>
  <div class="gavel-art" role="img" aria-label="Wooden judge's gavel"></div>
  <div class="phone-handset" role="img" aria-label="Telephone handset"></div>
  <div class="phone-cord" role="img" aria-label="Coiled telephone cord"></div>
  <div class="cta">
    <div class="free">Free Consultation</div>
    <div class="call">CAll: 808-472-3000</div>
  </div>

  <nav class="nav">
    <a class="current">Home</a>
    <a style="left:126px">About</a>
    <a style="left:224px">Services</a>
    <a style="left:339px">Testimonials</a>
    <a style="left:506px">Blog</a>
    <a style="left:596px">Contact</a>
  </nav>

  <main class="content">
    <div class="hero-art" role="img" aria-label="Banknotes with newspaper words: hardship, foreclosure, broke, bankruptcy, shake-up, trouble, unhappy"></div>

    <section class="consult-box">
      <h2>Free Consultation</h2>
      <p class="intro">Fill out the form below for a free no obli-<br>gation consultation, or call 808-472-3000</p>
      <div class="field" style="top:85px"><span>Your Name *</span><i></i></div>
      <div class="field" style="top:124px"><span>Your Email *</span><i></i></div>
      <div class="field" style="top:163px"><span>Your Phone *</span><i></i></div>
      <div class="field msg" style="top:202px"><span>Your Message</span><i></i></div>
      <div class="req">required *</div>
      <div class="submit">Submit</div>
    </section>

    <div class="welcome">
      <div class="video" role="img" aria-label="Video of the attorney speaking in his office">
        <svg width="36" height="26" viewBox="0 0 36 26"><rect width="36" height="26" rx="6" fill="#222" fill-opacity=".8"/><path d="M14 7 L24 13 L14 19 Z" fill="#fff"/></svg>
        <div class="bar"></div>
      </div>
      <span class="lead">Thanks for visiting us</span>.&nbsp; You came here because you are having <em>debt problems</em> and you want <em>solutions</em>.&nbsp; Yes, we want your business.&nbsp; But, we don't want it if it is not right for you.&nbsp; We have been at this a long time and assisted thousands of Hawaii people and families with their debt problems.&nbsp; Many of those people were referred by former clients, but, our biggest referral source is people who did not file a bankruptcy.&nbsp; The reason is simple- our absolutely <b>free</b> and confidential consultation will help you get a handle on your whole situation.&nbsp; We will discuss your assets, your debts, your income and expenses and get a complete picture.&nbsp; It is only with this complete global picture of your particular situation that you can know your options, all of them, and then you can decide what is right for you.&nbsp;&nbsp; You are the driver.&nbsp; Call us at 808-472-3000 (from all islands) and let us help you today!
    </div>

    <section class="testimonials">
      <h2>Testimonials</h2>
      <p>"Thanks for the good news about R's plan.... I<br>also want to say thank you for always treating<br>my mother with consideration.<br>remembered..."--HT</p>
      <p>"Thanks for the good news about R's plan.... I<br>also want to say thank you for always treating<br>my mother with consideration.<br>remembered..."--HT</p>
      <span class="more">view more</span>
    </section>
  </main>

  <footer class="footer">
    <div class="map-area" role="img" aria-label="Street map showing the office location in Honolulu"></div>
    <div class="address">
      <div class="firm">Daniel K. Halvorsen,</div>
      <div class="title">Attorney-at-Law</div>
      <div>2240 Kalena Ave. Suite 1410</div>
      <div>Honolulu, HI 96820</div>
      <div>808-472-3000</div>
      <div>info@plkwindra.com</div>
    </div>
    <div class="badge" role="img" aria-label="Professional association membership badge"></div>
    <div class="figure-art" role="img" aria-label="Figure breaking free from a chain and padlock"></div>
    <div class="legal"><b>Privacy Statement</b> Copyright 2012 Daniel K. Halvorsen</div>
  </footer>
</div>
</body>
</html>
```